Investment firm needs refreshed corporate powerpoint slides design

We need a new and refreshed powerpoint template for our corporate investment deck. We are a technology private equity group that primarily invests in fast growing software companies and we would like to reflect that in a modern and light blue / transparant / white powerpoint and fonts template. I have also attached our old investor deck as a guideline and also check out our website to get an idea of what we do and what type of companies we invested in. Please note that our website is old and so our presentation should be a refreshed "2017" modern design, not a copy / paste of our website design and graphics.
Updates

Project Deadline Extended Reason: I'm extending the deadline to February 27, but we would ideally receive something by the end of this week.Please submit updates. Thanks Added Tuesday, February 21, 2017

Target Market(s)

Investors such as high net worth individuals, pension funds, banks, financial advisors

Industry/Entity Type

Investment

Colors
33a6d7
85cae6
cfeae6
edf8f6
ffffff
fff3d1
86cfc6

Requirements
Must have
• We let you be creative, we trust you have seen more investment presentations before.
Nice to have
• Pre-built models, flow charts, graphs, charts, etc.
Should not have
• Fancy or edgy images, this has to be a modern, fresh and trustworthy looking powerpoint template. No stock images, if you do use stock images for background purposes please be creative! :-)

```html
<!DOCTYPE html>
<html lang="en">
<head>
<meta charset="utf-8">
<title>Halvard – Corporate Slide Template</title>
<link href="https://fonts.googleapis.com/css2?family=Montserrat:wght@500;600;700&family=Raleway:wght@300;400;500;600&display=swap" rel="stylesheet">
<style>
:root{
  --ink:#1e3a5c;
  --sea:#6aa9cb;
  --sea-deep:#5b9bbf;
  --sky:#8ec9e6;
  --teal:#86cfc6;
  --mint:#cfeae6;
  --foam:#edf8f6;
  --navy:#1c2b52;
  --gray:#8a96a3;
  --paper:#ffffff;
  --canvas:#f1f4f6;
}
*{margin:0;padding:0;box-sizing:border-box}
html,body{width:1106px;height:1200px;overflow:hidden;background:var(--canvas)}
body{position:relative;font-family:"Raleway",sans-serif;color:var(--ink)}

.slide{position:absolute;width:345px;height:194px;background:var(--paper);overflow:hidden;box-shadow:0 1px 4px rgba(30,58,92,.18)}
.c0{left:11px}.c1{left:379px}.c2{left:747px}
.r0{top:3px}.r1{top:203px}.r2{top:403px}.r3{top:603px}.r4{top:803px}.r5{top:1003px}

.abs{position:absolute}
.photo{position:absolute}
.brand{position:absolute;font-family:"Raleway",sans-serif;font-weight:500;color:var(--ink);letter-spacing:.2px}
.brand.corner{right:12px;top:11px;font-size:17px}
.brand.light{color:var(--paper)}

.head{position:absolute;left:15px;top:12px;font:600 15px "Montserrat",sans-serif;color:var(--ink)}
.head::after{content:"";position:absolute;left:1px;bottom:-6px;width:14px;height:2px;background:var(--teal)}
.page::before{content:"";position:absolute;left:0;top:14px;border-top:6px solid transparent;border-bottom:6px solid transparent;border-left:6px solid #b9c6d2}

.foot{position:absolute;left:0;right:0;bottom:0;height:9px;background:var(--sky);display:flex;justify-content:space-between;align-items:center;padding:0 6px;font:400 3.5px "Raleway",sans-serif;color:var(--paper)}
.foot .num{background:var(--paper);color:var(--gray);width:12px;text-align:center;line-height:9px}
.foot.dark{background:var(--navy)}

.tiny{font:300 4px/1.4 "Raleway",sans-serif;color:var(--gray)}
.tiny.w{color:rgba(255,255,255,.85)}
.label{font:500 6px "Raleway",sans-serif;color:var(--ink)}
.label.w{color:var(--paper)}
.icon{position:absolute;width:10px;height:10px;border-radius:50%;background:var(--sea);display:flex;align-items:center;justify-content:center}
.icon.sq{border-radius:1px}
.icon svg{width:6px;height:6px}
.icon.dark{background:var(--navy)}
.icon.ink{background:var(--ink)}

/* slide 1 */
.cover{background:linear-gradient(150deg,#7fb4cf 0%,#79b9c8 55%,#86cfc6 100%)}
.cover .brand{left:118px;top:66px;font-size:50px;color:var(--paper);font-weight:400}

/* slide 2 */
.title-band .photo{left:0;top:0;width:345px;height:146px;background:linear-gradient(160deg,#8ab8d2,#6aa9cb 60%,#7fb7c9)}
.title-band .t{left:12px;top:84px;font:400 15px "Raleway",sans-serif;color:var(--paper)}
.title-band .st{left:91px;top:101px;font:300 5px "Raleway",sans-serif;color:var(--paper)}
.title-band .brand{left:34px;top:148px;font-size:30px}
.title-band .strip{left:0;bottom:0;width:345px;height:7px;background:var(--sky)}
.presenter{position:absolute;display:flex;align-items:center;gap:2px;font:500 4.5px "Raleway",sans-serif;color:var(--ink)}
.presenter i{width:5px;height:5px;border-radius:50%;background:var(--ink);display:block}
.presenter small{display:block;font-size:3px;color:var(--gray)}

/* slide 3 */
.hero .photo{left:0;top:0;width:345px;height:176px;background:linear-gradient(120deg,#e8f0f5 0%,#c9dfeb 45%,#a9cbe0 100%)}
.hero .topbar{left:0;top:0;width:345px;height:33px;background:var(--paper)}
.hero .brand{left:46px;top:6px;font-size:26px}
.hero .band{left:0;top:136px;width:345px;height:32px;background:rgba(106,169,203,.85)}
.hero .t{left:0;width:345px;top:140px;text-align:center;font:600 14px "Montserrat",sans-serif;color:var(--paper)}
.hero .st{left:0;width:345px;top:158px;text-align:center;font:600 4.5px "Raleway",sans-serif;color:var(--paper)}
.hero .strip{left:0;bottom:0;width:345px;height:4px;background:var(--sky)}

/* slide 4 */
.quote-full{background:linear-gradient(150deg,#7fb4cf,#86cfc6)}
.quote-full .mark{left:157px;top:48px;width:32px;height:32px;border-radius:50%;background:var(--paper);color:var(--sea);font:700 22px/40px "Montserrat",sans-serif;text-align:center}
.quote-full .q{left:0;width:345px;top:89px;text-align:center;font:300 11px/1.25 "Raleway",sans-serif;color:var(--paper)}
.quote-full .by{left:0;width:345px;top:143px;text-align:center;font:300 5px "Raleway",sans-serif;color:rgba(255,255,255,.85)}

/* agenda */
.agenda .item{position:absolute;width:120px}
.agenda .item .icon{left:0;top:1px}
.agenda .item .txt{margin-left:20px}
.agenda .item .label{font-size:6.5px}

/* about */
.about .photo{left:0;top:0;width:172px;height:185px;background:linear-gradient(160deg,#d9e7ef,#a9c7da 70%,#8fb6cf)}
.about .box{left:172px;top:42px;width:173px;height:110px;background:var(--sea);padding:20px 14px}
.about .box h3{font:600 15px "Montserrat",sans-serif;color:var(--paper);margin-bottom:10px}
.about .box p{margin-bottom:5px}

/* services */
.services .tile{left:32px;top:45px;width:135px;height:84px;background:var(--sea)}
.services .tile .brand{left:38px;top:30px;font-size:18px;color:var(--ink)}
.services .below{left:32px;top:135px;width:135px}
.services .svc{position:absolute;left:190px;width:145px}
.services .svc .icon{left:0;top:1px;width:12px;height:12px}
.services .svc .txt{margin-left:22px}

/* quote area */
.qarea .panel{left:0;top:42px;width:345px;height:123px;background:var(--sea)}
.qarea .photo{left:173px;top:42px;width:172px;height:123px;background:linear-gradient(130deg,#eaf2f7,#b8d4e4 60%,#7fb4d3)}
.qarea .q{left:28px;top:78px;font:300 8px/1.3 "Raleway",sans-serif;color:var(--paper);width:140px}
.qarea .by{left:32px;top:131px;font:300 4.5px "Raleway",sans-serif;color:rgba(255,255,255,.85)}

/* previous work */
.work .badge{position:absolute;width:52px;height:30px}
.work .badge.round{width:32px;height:32px;border-radius:50%;border:2px solid var(--navy)}
.work .badge.bar{background:var(--navy);height:14px;border-radius:1px}
.work .badge.frame{border:2px solid var(--navy);height:22px}
.work .badge.pale{border:1.5px solid #b7c0c9;height:14px;border-radius:7px}
.work .centre{left:87px;top:66px;width:172px;height:62px;background:var(--sea);color:var(--paper);font:600 15px/62px "Montserrat",sans-serif;text-align:center}

/* text area */
.textarea .lead{left:29px;top:61px;width:290px;font:600 6.5px/1.35 "Raleway",sans-serif;color:var(--ink)}
.textarea .body{left:29px;top:89px;width:290px}
.textarea .body p{margin-bottom:5px;font-size:4.5px}

/* vision */
.vision .panel{left:0;top:42px;width:345px;height:128px;background:linear-gradient(120deg,#6aa9cb,#7fb2d0)}
.vision .col{position:absolute;top:66px}
.vision .kicker{font:300 8px "Raleway",sans-serif;color:var(--paper);margin-bottom:6px}
.vision .strong{font:600 6.5px/1.3 "Raleway",sans-serif;color:var(--paper);margin-bottom:8px}
.vision .m{position:absolute;left:0;width:135px}
.vision .m .icon{background:var(--paper);left:0;top:0;width:12px;height:12px}
.vision .m .txt{margin-left:20px}

/* split title */
.split .photo{left:0;top:0;width:172px;height:185px;background:linear-gradient(150deg,#eef4f8,#c4dae7 60%,#9fc3d9)}
.split .box{left:0;top:64px;width:172px;height:118px;background:rgba(106,169,203,.75)}
.split .brand{left:48px;top:80px;font-size:24px}
.split .t{left:185px;top:50px;font:600 11px "Montserrat",sans-serif;color:var(--ink)}
.split .pt{position:absolute;left:188px;width:140px}
.split .pt .icon{left:0;top:0;width:9px;height:9px;background:var(--navy);color:#fff;font:600 4px/9px "Raleway",sans-serif;text-align:center}
.split .pt .txt{margin-left:20px}

/* tile grid */
.grid6 .cell{position:absolute;width:96px;height:58px;padding:8px}
.grid6 .cell .label{font-size:5px;margin-bottom:4px}
.ph-a{background:linear-gradient(140deg,#e6eff5,#a7c8dc)}
.ph-b{background:linear-gradient(140deg,#f2f6f9,#b9d0df)}

/* meridian */
.meridian .photo{left:0;top:0;width:173px;height:194px;background:linear-gradient(130deg,#c9d6de,#9fb2c0 50%,#e6ecf0)}
.meridian .panel{left:173px;top:0;width:172px;height:194px;background:var(--navy);padding:11px 10px 0 14px}
.meridian .name{text-align:right;font:600 9px "Montserrat",sans-serif;color:var(--paper);letter-spacing:1px;margin-bottom:7px}
.meridian .lead{font:600 7px/1.3 "Montserrat",sans-serif;color:var(--paper);margin-bottom:7px}
.meridian .row{position:relative;padding-left:19px;margin-bottom:5px;min-height:22px}
.meridian .row svg{position:absolute;left:0;top:0;width:11px;height:11px}

/* portrait collage */
.collage .p1{left:4px;top:4px;width:111px;height:88px;background:linear-gradient(150deg,#8dbcd6,#6aa9cb)}
.collage .brand{left:27px;top:36px;font-size:24px}
.collage .p2{left:4px;top:95px;width:111px;height:89px;background:linear-gradient(140deg,#c8d8e2,#9db5c4)}
.collage .p3{left:118px;top:4px;width:123px;height:180px;background:linear-gradient(160deg,#eef2f5,#c8d3dc 60%,#55677e)}
.collage .t{left:250px;top:30px;font:600 14px/1.1 "Montserrat",sans-serif;color:var(--ink)}
.collage .body{left:250px;top:70px;width:88px}
.collage .body p{margin-bottom:4px}

/* titled text + photo */
.textphoto .lead{left:28px;top:62px;width:120px;font:600 6.5px/1.35 "Raleway",sans-serif}
.textphoto .body{left:28px;top:107px;width:120px}
.textphoto .body p{margin-bottom:5px}
.textphoto .photo{left:172px;top:52px;width:168px;height:113px;background:linear-gradient(120deg,#eef4f8,#c3d9e6 50%,#a5c6da)}

/* portfolio */
.portfolio .sub{left:18px;top:42px;width:140px}
.portfolio .row{position:absolute;left:28px;width:120px}
.portfolio .row .icon{left:0;top:1px;width:10px;height:10px}
.portfolio .row .txt{margin-left:18px}
.portfolio .a{left:173px;top:4px;width:84px;height:176px;background:linear-gradient(170deg,#f3f5f7,#aab6c0 55%,#2f3d4e)}
.portfolio .b{left:259px;top:4px;width:82px;height:176px;background:linear-gradient(170deg,#eef1f4,#9aa8b5 55%,#2a3849)}

/* differences */
.diff .panel{left:17px;top:64px;width:311px;height:97px;background:var(--sea)}
.diff .photo{left:198px;top:70px;width:124px;height:63px;background:linear-gradient(130deg,#f1f6f9,#bcd5e4)}
.diff .row{position:absolute;left:30px;width:160px}
.diff .row .icon{left:0;top:0;background:var(--navy)}
.diff .row .txt{margin-left:20px}
</style>
</head>
<body>

<!-- 1 cover -->
<section class="slide cover c0 r0" role="img" aria-label="Cover slide over a soft teal photo of a glass office tower">
  <div class="brand">Halvard</div>
</section>

<!-- 2 title band -->
<section class="slide title-band c1 r0">
  <div class="photo" role="img" aria-label="Blue-toned photo of a glass skyscraper"></div>
  <div class="abs t">Your Title Goes Here</div>
  <div class="abs st">Your Subtitle Goes Here</div>
  <div class="brand">Halvard</div>
  <div class="presenter" style="left:268px;top:170px"><i></i><div>Tom Ellis<small>VP Marketing</small></div></div>
  <div class="presenter" style="left:313px;top:170px"><i></i><div>Anna Reed<small>Senior Analyst</small></div></div>
  <div class="abs strip"></div>
</section>

<!-- 3 hero -->
<section class="slide hero c2 r0">
  <div class="photo" role="img" aria-label="Photo of a business man in a suit holding a tablet"></div>
  <div class="abs topbar"></div>
  <div class="brand">Halvard</div>
  <div class="abs band"></div>
  <div class="abs t">Your Title Goes Here</div>
  <div class="abs st">Your Subtitle Goes Here</div>
  <div class="presenter" style="left:28px;top:181px"><i></i><div>Tom Ellis<small>VP Marketing</small></div></div>
  <div class="presenter" style="left:88px;top:181px"><i></i><div>Anna Reed<small>Senior Analyst</small></div></div>
  <div class="presenter" style="left:198px;top:181px"><i></i><div>Mark Doyle<small>Vice President</small></div></div>
  <div class="abs tiny" style="right:8px;top:184px">City | November 28, 2017</div>
  <div class="abs strip"></div>
</section>

<!-- 4 quote -->
<section class="slide quote-full c0 r1" role="img" aria-label="Quote slide over a teal photo of a man at an office window">
  <div class="abs mark">“</div>
  <div class="abs q">Coming together is a beginning.<br>Keeping together is progress.<br>Working together is success.</div>
  <div class="abs by">- A. Whitmore -</div>
</section>

<!-- 5 agenda -->
<section class="slide page agenda c1 r1">
  <div class="head">Our Agenda</div>
  <div class="brand corner">Halvard</div>
  <div class="item" style="left:46px;top:55px"><span class="icon sq"><svg viewBox="0 0 10 10"><circle cx="5" cy="5" r="3.5" fill="none" stroke="#fff"/><path d="M5 3v2.2l1.4 1" stroke="#fff" fill="none"/></svg></span><div class="txt"><div class="label">Agenda One</div><div class="tiny">Short note on the first topic of the day and the key aims.</div></div></div>
  <div class="item" style="left:46px;top:96px"><span class="icon sq"><svg viewBox="0 0 10 10"><circle cx="5" cy="5" r="3.5" fill="none" stroke="#fff"/><path d="M5 3v2.2l1.4 1" stroke="#fff" fill="none"/></svg></span><div class="txt"><div class="label">Agenda Two</div><div class="tiny">Short note on the second topic of the day and the key aims.</div></div></div>
  <div class="item" style="left:46px;top:136px"><span class="icon sq"><svg viewBox="0 0 10 10"><circle cx="5" cy="5" r="3.5" fill="none" stroke="#fff"/><path d="M5 3v2.2l1.4 1" stroke="#fff" fill="none"/></svg></span><div class="txt"><div class="label">Agenda Three</div><div class="tiny">Short note on the third topic of the day and the key aims.</div></div></div>
  <div class="item" style="left:185px;top:55px"><span class="icon sq"><svg viewBox="0 0 10 10"><circle cx="5" cy="5" r="3.5" fill="none" stroke="#fff"/><path d="M5 3v2.2l1.4 1" stroke="#fff" fill="none"/></svg></span><div class="txt"><div class="label">Agenda Four</div><div class="tiny">Short note on the fourth topic of the day and the key aims.</div></div></div>
  <div class="item" style="left:185px;top:96px"><span class="icon sq"><svg viewBox="0 0 10 10"><circle cx="5" cy="5" r="3.5" fill="none" stroke="#fff"/><path d="M5 3v2.2l1.4 1" stroke="#fff" fill="none"/></svg></span><div class="txt"><div class="label">Agenda Five</div><div class="tiny">Short note on the fifth topic of the day and the key aims.</div></div></div>
  <div class="item" style="left:185px;top:136px"><span class="icon sq"><svg viewBox="0 0 10 10"><circle cx="5" cy="5" r="3.5" fill="none" stroke="#fff"/><path d="M5 3v2.2l1.4 1" stroke="#fff" fill="none"/></svg></span><div class="txt"><div class="label">Agenda Six</div><div class="tiny">Short note on the sixth topic of the day and the key aims.</div></div></div>
  <div class="foot"><span>© 2017 HALVARD. All rights reserved</span><span class="num">5</span></div>
</section>

<!-- 6 about -->
<section class="slide about c2 r1">
  <div class="photo" role="img" aria-label="Photo of a business man in a suit holding a tablet"></div>
  <div class="brand corner">Halvard</div>
  <div class="abs box">
    <h3>About Us</h3>
    <p class="tiny w">We back fast growing software firms with capital, know-how and a long view on value.</p>
    <p class="tiny w">Our team works side by side with founders to build lasting market leaders.</p>
  </div>
  <div class="foot"><span>© 2017 HALVARD. All rights reserved</span><span class="num">6</span></div>
</section>

<!-- 7 services -->
<section class="slide page services c0 r2">
  <div class="head">Our Services</div>
  <div class="brand corner">Halvard</div>
  <div class="abs tile"><div class="brand">Halvard</div></div>
  <div class="abs below"><div class="label" style="font-size:5.5px">Your Title Goes Here</div><div class="tiny">A brief line about the service we offer and how it helps each firm grow in its market.</div></div>
  <div class="svc" style="top:49px"><span class="icon"><svg viewBox="0 0 10 10"><path d="M2 8V6M4 8V4M6 8V5M8 8V2" stroke="#fff"/></svg></span><div class="txt"><div class="label">Service Number One</div><div class="tiny">A brief line about this service and the value it brings to our partners.</div></div></div>
  <div class="svc" style="top:90px"><span class="icon"><svg viewBox="0 0 10 10"><path d="M2 8l6-6M5 2h3v3" stroke="#fff" fill="none"/></svg></span><div class="txt"><div class="label">Service Number Two</div><div class="tiny">A brief line about this service and the value it brings to our partners.</div></div></div>
  <div class="svc" style="top:131px"><span class="icon"><svg viewBox="0 0 10 10"><circle cx="4.3" cy="4.3" r="2.5" fill="none" stroke="#fff"/><path d="M6 6l2.3 2.3" stroke="#fff"/></svg></span><div class="txt"><div class="label">Service Number Three</div><div class="tiny">A brief line about this service and the value it brings to our partners.</div></div></div>
  <div class="foot"><span>© 2017 HALVARD. All rights reserved</span><span class="num">7</span></div>
</section>

<!-- 8 quote area -->
<section class="slide page qarea c1 r2">
  <div class="head">Quote Area</div>
  <div class="brand corner">Halvard</div>
  <div class="abs panel"></div>
  <div class="photo" role="img" aria-label="Photo of printed pie and bar charts on a desk"></div>
  <div class="abs q">“ Coming together is a beginning.<br>Keeping together is progress.<br>Working together is success.</div>
  <div class="abs by">- A. Whitmore</div>
  <div class="foot"><span>© 2017 HALVARD. All rights reserved</span><span class="num">8</span></div>
</section>

<!-- 9 previous work -->
<section class="slide work c2 r2">
  <div class="badge frame" style="left:16px;top:16px"></div>
  <div class="badge bar" style="left:106px;top:24px"></div>
  <div class="badge frame" style="left:192px;top:16px"></div>
  <div class="badge bar" style="left:278px;top:24px;width:50px"></div>
  <div class="badge frame" style="left:16px;top:84px;width:40px"></div>
  <div class="badge pale" style="left:282px;top:90px;width:46px"></div>
  <div class="badge round" style="left:24px;top:146px"></div>
  <div class="badge round" style="left:112px;top:146px"></div>
  <div class="badge frame" style="left:188px;top:150px"></div>
  <div class="badge round" style="left:292px;top:146px"></div>
  <div class="abs centre">Our Previous work</div>
</section>

<!-- 10 text area -->
<section class="slide page textarea c0 r3">
  <div class="head">Text Area</div>
  <div class="brand corner">Halvard</div>
  <div class="abs lead">This is place for your header text. Insert your text here, just replace this text with your own text</div>
  <div class="abs body tiny">
    <p>We invest in software firms with strong teams, loyal clients and room to scale. Our support spans strategy, hiring, pricing and the steps needed to enter new markets across Europe and beyond.</p>
    <p>Each deal is built on trust, clear goals and shared reporting, so our partners always know where the business stands and what the next stage of growth will need.</p>
    <p>We stay close to the numbers and closer to the people behind them.</p>
  </div>
  <div class="foot"><span>© 2017 HALVARD. All rights reserved</span><span class="num">10</span></div>
</section>

<!-- 11 vision & mission -->
<section class="slide page vision c1 r3">
  <div class="head">Our Vision &amp; Mission</div>
  <div class="brand corner">Halvard</div>
  <div class="abs panel" role="img" aria-label="Blue-toned photo of a hand over a growth chart"></div>
  <div class="col" style="left:22px;width:140px">
    <div class="kicker">• Our Vision:</div>
    <div class="strong">Go to the Next Level<br>Without look in the past</div>
    <div class="tiny w">We aim to be the partner of choice for software founders who want to grow with focus, calm and the right capital at each stage.</div>
  </div>
  <div class="col" style="left:190px;width:140px">
    <div class="kicker">• Our Missions:</div>
    <div class="m" style="top:14px"><span class="icon"></span><div class="txt"><div class="label w" style="font-size:4.5px">Your Text Here</div><div class="tiny w">Back firms with clear growth plans.</div></div></div>
    <div class="m" style="top:40px"><span class="icon"></span><div class="txt"><div class="label w" style="font-size:4.5px">Your Text Here</div><div class="tiny w">Build teams that scale with care.</div></div></div>
    <div class="m" style="top:67px"><span class="icon"></span><div class="txt"><div class="label w" style="font-size:4.5px">Your Text Here</div><div class="tiny w">Deliver steady long term returns.</div></div></div>
  </div>
  <div class="foot"><span>© 2017 HALVARD. All rights reserved</span><span class="num">11</span></div>
</section>

<!-- 12 split title -->
<section class="slide split c2 r3">
  <div class="photo" role="img" aria-label="Photo of a man standing at a bright office window"></div>
  <div class="abs box"></div>
  <div class="brand">Halvard</div>
  <div class="brand corner">Halvard</div>
  <div class="abs t">Your Title Goes Here</div>
  <div class="pt" style="top:83px"><span class="icon">1</span><div class="txt"><div class="label" style="font-size:5px">Your Text Here</div><div class="tiny">A short line on the first point, what it means and why it matters now.</div></div></div>
  <div class="pt" style="top:131px"><span class="icon">2</span><div class="txt"><div class="label" style="font-size:5px">Your Text Here</div><div class="tiny">A short line on the second point, what it means and why it matters now.</div></div></div>
  <div class="foot"><span>© 2017 HALVARD. All rights reserved</span><span class="num">12</span></div>
</section>

<!-- 13 tile grid -->
<section class="slide page grid6 c0 r4">
  <div class="head">Your Title Goes Here</div>
  <div class="brand corner">Halvard</div>
  <div class="cell ph-a" style="left:25px;top:50px" role="img" aria-label="Photo of a man by an office window"></div>
  <div class="cell" style="left:124px;top:50px;background:var(--teal)"><div class="label w">Heading Goes Here</div><div class="tiny w">A short line on this topic and the value it adds for you.</div></div>
  <div class="cell ph-b" style="left:223px;top:50px" role="img" aria-label="Photo of printed bar charts"></div>
  <div class="cell" style="left:25px;top:113px;background:var(--sea)"><div class="label w">Heading Goes Here</div><div class="tiny w">A short line on this topic and the value it adds for you.</div></div>
  <div class="cell ph-a" style="left:124px;top:113px" role="img" aria-label="Photo of glasses and a pen on a report"></div>
  <div class="cell" style="left:223px;top:113px;background:#a9b2ba"><div class="label w">Heading Goes Here</div><div class="tiny w">A short line on this topic and the value it adds for you.</div></div>
  <div class="foot"><span>© 2017 HALVARD. All rights reserved</span><span class="num">13</span></div>
</section>

<!-- 14 meridian -->
<section class="slide meridian c1 r4">
  <div class="photo" role="img" aria-label="Photo of two business people shaking hands"></div>
  <div class="abs panel">
    <div class="name">MERIDIAN</div>
    <div class="lead">This is place for your header text. Insert your text here, just replace this text with your own text</div>
    <div class="row"><svg viewBox="0 0 10 10"><circle cx="4.2" cy="4.2" r="3" fill="none" stroke="#fff" stroke-width="1.2"/><path d="M6.4 6.4L9 9" stroke="#fff" stroke-width="1.2"/></svg><div class="label w" style="font-size:4.5px">Your Text Here</div><div class="tiny w">A short line of text to go here.</div></div>
    <div class="row"><svg viewBox="0 0 10 10"><path d="M2 8l1-3 5-5 2 2-5 5z" fill="#fff"/></svg><div class="label w" style="font-size:4.5px">Your Text Here</div><div class="tiny w">A short line of text to go here.</div></div>
    <div class="row"><svg viewBox="0 0 10 10"><path d="M1 9l8-8M5 1h4v4" stroke="#fff" stroke-width="1.2" fill="none"/></svg><div class="label w" style="font-size:4.5px">Your Text Here</div><div class="tiny w">A short line of text to go here.</div></div>
    <div class="row"><svg viewBox="0 0 10 10"><circle cx="5" cy="5" r="3" fill="none" stroke="#fff" stroke-width="2" stroke-dasharray="2 1.2"/><circle cx="5" cy="5" r="1.2" fill="#fff"/></svg><div class="label w" style="font-size:4.5px">Your Text Here</div><div class="tiny w">A short line of text to go here.</div></div>
  </div>
</section>

<!-- 15 collage -->
<section class="slide collage c2 r4">
  <div class="photo p1" role="img" aria-label="Blue-toned photo of a man at an office window"></div>
  <div class="brand">Halvard</div>
  <div class="photo p2" role="img" aria-label="Photo of business people meeting in an office"></div>
  <div class="photo p3" role="img" aria-label="Portrait photo of a smiling business man in a suit"></div>
  <div class="abs t">Your Title<br>Goes Here</div>
  <div class="abs body tiny">
    <p>We help software firms grow with patient capital and hands on support.</p>
    <p>Our team brings deep sector know-how to every board seat.</p>
    <p>Clear goals and open reporting guide each step.</p>
  </div>
  <div class="foot dark"><span>© 2017 MERIDIAN. All rights reserved</span><span class="num">15</span></div>
</section>

<!-- 16 text + photo -->
<section class="slide page textphoto c0 r5">
  <div class="head">Your Title Goes Here</div>
  <div class="brand corner">Halvard</div>
  <div class="abs lead">This is place for your header text. Insert your text here, just replace this text with your own text</div>
  <div class="abs body tiny">
    <p>We invest in software firms with strong teams and clear growth plans, adding capital and hands on help.</p>
    <p>Every deal rests on trust, shared goals and open reporting.</p>
  </div>
  <div class="photo" role="img" aria-label="Blue-toned photo of people in a glass office hall"></div>
  <div class="foot"><span>© 2017 HALVARD. All rights reserved</span><span class="num">16</span></div>
</section>

<!-- 17 portfolio -->
<section class="slide page portfolio c1 r5">
  <div class="head">Portfolio Area</div>
  <div class="abs sub"><div class="label" style="font-size:5.5px">Heading Goes Here</div><div class="tiny">A short line about this group of firms and what they share in common.</div></div>
  <div class="row" style="top:76px"><span class="icon"><svg viewBox="0 0 10 10"><circle cx="4.3" cy="4.3" r="2.5" fill="none" stroke="#fff"/><path d="M6 6l2.3 2.3" stroke="#fff"/></svg></span><div class="txt"><div class="label" style="font-size:5px">Your Text Here</div><div class="tiny">A short line of text to go here.</div></div></div>
  <div class="row" style="top:101px"><span class="icon"><svg viewBox="0 0 10 10"><path d="M2 8l1-3 4-4 2 2-4 4z" fill="#fff"/></svg></span><div class="txt"><div class="label" style="font-size:5px">Your Text Here</div><div class="tiny">A short line of text to go here.</div></div></div>
  <div class="row" style="top:126px"><span class="icon"><svg viewBox="0 0 10 10"><path d="M2 8l6-6M5 2h3v3" stroke="#fff" fill="none"/></svg></span><div class="txt"><div class="label" style="font-size:5px">Your Text Here</div><div class="tiny">A short line of text to go here.</div></div></div>
  <div class="row" style="top:151px"><span class="icon"><svg viewBox="0 0 10 10"><circle cx="5" cy="5" r="2.6" fill="none" stroke="#fff" stroke-width="1.6" stroke-dasharray="1.6 1"/></svg></span><div class="txt"><div class="label" style="font-size:5px">Your Text Here</div><div class="tiny">A short line of text to go here.</div></div></div>
  <div class="photo a" role="img" aria-label="Photo of business people in silhouette by a window"></div>
  <div class="photo b" role="img" aria-label="Photo of a team in silhouette at a meeting table"></div>
  <div class="foot"><span>© 2017 HALVARD. All rights reserved</span><span class="num">17</span></div>
</section>

<!-- 18 differences -->
<section class="slide page diff c2 r5">
  <div class="head">Our Differences</div>
  <div class="brand corner">Halvard</div>
  <div class="abs panel"></div>
  <div class="photo" role="img" aria-label="Photo of a man at an office window with a world map overlay"></div>
  <div class="row" style="top:70px"><span class="icon"><svg viewBox="0 0 10 10"><path d="M2 8l6-6M5 2h3v3" stroke="#fff" fill="none"/></svg></span><div class="txt tiny w">We back firms early and stay for the long run, adding value at each stage.</div></div>
  <div class="row" style="top:92px"><span class="icon"><svg viewBox="0 0 10 10"><circle cx="5" cy="5" r="2.6" fill="none" stroke="#fff" stroke-width="1.6" stroke-dasharray="1.6 1"/></svg></span><div class="txt tiny w">Deep sector focus on fast growing software and data firms.</div></div>
  <div class="row" style="top:114px"><span class="icon"><svg viewBox="0 0 10 10"><path d="M2 8l1-3 4-4 2 2-4 4z" fill="#fff"/></svg></span><div class="txt tiny w">Hands on support in hiring, pricing and new market entry.</div></div>
  <div class="row" style="top:136px"><span class="icon"><svg viewBox="0 0 10 10"><circle cx="4.3" cy="4.3" r="2.5" fill="none" stroke="#fff"/><path d="M6 6l2.3 2.3" stroke="#fff"/></svg></span><div class="txt tiny w">Open reporting and clear goals shared with every partner.</div></div>
  <div class="foot"><span>© 2017 HALVARD. All rights reserved</span><span class="num">18</span></div>
</section>

</body>
</html>
```